Spring Style Exclusive Shopping Party for women

We need a postcard design for our Spring Shopping Event. Lark Meadow is a women's apparel and accessories store featuring missy, petite and plus sizes. Event is Saturday, April 1 from 9am-10am. Looking for a twist on the spring shopping party idea. Attaching 2 postcards we have previously sent for this event and 2 ideas for what we are looking for in new postcard.

Target Market(s)

women 20+

Industry/Entity Type

Retail

Font styles to use
Serif

Requirements
Must have
• must be eye catching, have the logo, date and time of event,
Nice to have
• woman model

```html
<!DOCTYPE html>
<html lang="en">
<head>
<meta charset="utf-8">
<title>Lark Meadow Spring Shopping Party Postcard</title>
<link rel="stylesheet" href="https://fonts.googleapis.com/css2?family=Playfair+Display:ital,wght@0,400;0,700;1,400&family=Open+Sans:wght@400;600&display=swap">
<style>
:root{
  --bg:#2b2622;
  --red:#d71f2b;
  --ink:#2a2a2a;
  --cream:#f7f3ec;
  --white:#ffffff;
  --blue:#1f7fc4;
  --grey:#c9c9c9;
  --petal-pink:#f2a7b8;
  --petal-peach:#f6cfa4;
  --leaf:#a9c98a;
}
*{margin:0;padding:0;box-sizing:border-box}
html,body{width:816px;height:1200px;overflow:hidden;background:var(--bg)}
.canvas{position:relative;width:816px;height:1200px}
.card{position:absolute;left:49px;width:713px;height:571px;overflow:hidden;box-shadow:0 6px 18px rgba(0,0,0,.45)}
.card--front{top:14px;background:var(--cream)}
.card--back{top:612px;background:var(--white)}
.serif{font-family:"Playfair Display",Georgia,serif}
.sans{font-family:"Open Sans",Arial,sans-serif}

/* front */
.frame{position:absolute;left:11px;top:19px;right:11px;bottom:27px;border:3px solid var(--red)}
.florals{position:absolute;border-radius:50%;filter:blur(2px)}
.florals--top{left:-40px;top:-50px;width:345px;height:280px;
  background:radial-gradient(circle at 45% 50%,var(--petal-pink) 0 30%,var(--petal-peach) 45%,var(--leaf) 62%,rgba(169,201,138,0) 72%)}
.florals--bottom{left:468px;top:380px;width:300px;height:240px;
  background:radial-gradient(circle at 50% 50%,var(--petal-peach) 0 28%,var(--petal-pink) 45%,var(--leaf) 62%,rgba(169,201,138,0) 72%)}
.brand{position:absolute;display:flex;align-items:center;gap:10px;color:var(--red);font-weight:700}
.brand__dot{width:16px;height:16px;border-radius:50%;background:var(--red)}
.card--front .brand{left:420px;top:45px;font-size:46px}
.card--front .brand-url{position:absolute;left:458px;top:105px;font-size:13px;color:var(--ink)}
.event-date{position:absolute;left:264px;top:206px;font-size:44px;color:var(--red)}
.event-time{position:absolute;left:420px;top:258px;font-size:34px;font-style:italic;color:var(--red)}
.intro{position:absolute;left:36px;top:372px;font-size:23px;line-height:42px;color:var(--red)}
.site{position:absolute;left:36px;top:500px;font-size:21px;color:var(--red)}

/* back */
.card--back .brand{left:24px;top:18px;font-size:36px}
.card--back .brand-url{position:absolute;left:52px;top:64px;font-size:10px;color:var(--ink)}
.swoosh{position:absolute;left:0;top:0}
.offer{position:absolute;left:24px;top:92px;font-size:46px;font-weight:700;color:var(--red);line-height:1}
.offer-sub{position:absolute;left:24px;top:136px;font-size:34px;color:var(--ink);line-height:1.1}
.offer-date{position:absolute;left:24px;top:176px;font-size:17px;color:var(--red)}
.offer-copy{position:absolute;left:24px;top:202px;width:300px;font-size:13px;line-height:18px;color:var(--ink)}
.band{position:absolute;left:0;top:313px;width:100%;height:46px;background:var(--blue)}
.band__text{position:absolute;left:24px;top:317px;width:290px;font-size:13px;line-height:18px;color:var(--white)}
.rsvp{position:absolute;left:24px;top:369px;width:300px;font-size:13px;line-height:18px;color:var(--ink)}
.store{position:absolute;left:24px;top:436px;font-size:13px;line-height:20px;color:var(--ink)}
.store__city{color:var(--red);font-weight:600}
.stamp{position:absolute;left:617px;top:19px;width:80px;height:82px;border:2px dashed var(--grey)}
</style>
</head>
<body>
<main class="canvas">

  <section class="card card--front">
    <div class="florals florals--top" role="img" aria-label="Watercolor spring flowers in pink and peach with green leaves"></div>
    <div class="florals florals--bottom" role="img" aria-label="Watercolor spring flowers in peach and pink with green leaves"></div>
    <div class="frame"></div>
    <div class="brand serif"><span class="brand__dot"></span>Lark Meadow</div>
    <div class="brand-url sans">www.larkmeadowshop.com</div>
    <h1 class="event-date serif">Saturday, 1st April</h1>
    <p class="event-time serif">From 9am-10am</p>
    <p class="intro sans">Lark Meadow is a women's apparel<br>and accessories store featuring<br>missy, petite and plus sizes.</p>
    <p class="site sans">www.larkmeadowshop.com</p>
  </section>

  <section class="card card--back">
    <svg class="swoosh" width="713" height="571" viewBox="0 0 713 571" aria-hidden="true">
      <path d="M300 0 C385 160 385 410 300 571 L318 571 C403 410 403 160 318 0 Z" fill="var(--grey)"/>
      <path d="M322 0 C410 160 410 410 322 571 L350 571 C438 410 438 160 350 0 Z" fill="var(--red)"/>
    </svg>
    <div class="brand serif"><span class="brand__dot"></span>Lark Meadow</div>
    <div class="brand-url sans">www.larkmeadowshop.com</div>
    <div class="stamp"></div>
    <p class="offer serif">30% OFF</p>
    <p class="offer-sub serif">your entire purchase</p>
    <p class="offer-date serif">Saturday, 1st April From 9am-10am</p>
    <p class="offer-copy sans">Join us for our special early opening - only FOR our FAVORITE SHOPAHOLICS! Everyone will receive a gift bag plus great savings opportunities during this event.</p>
    <div class="band"></div>
    <p class="band__text sans">Pastries and juice will be served to start your day off right!</p>
    <p class="rsvp sans">Please RSVP by Sept. 7 at 555-014-2290. Guests are welcome although reservations are required as seating is limited.</p>
    <p class="store sans"><span class="store__city">FAIRHAVEN</span><br>118 W Orchard Ln<br>555-014-2290</p>
  </section>

</main>
</body>
</html>
```